Graphic Design for Application Form and Menu

We are a success education company called Tandem Crestline. We are designing a USB application for a personal development program that will be cross platform (PC/Mac). The product is called Quiet Harvest, Meridale Academy (These logos are already created). The program will open pdf books in a Flash reader, play audio and video files in the default media player, and open windows for recording entries in a journal and for setting goals.
We need a graphic design for a small control panel (300px X 300px) to launch the different modules of the program.

We are looking for a design that is clean and professional.
A sample is included of everything that needs to be on the form. A sample menu is also included. We are looking for other designs for the form and menu.
Updates

Industry/Entity Type

Graphic Design

Requirements
Must have
• The panel will have: a menu, two toolbars, and two status panels.
ItemDetails:
A menu will have items for "Welcome, Profile, and Kudos."
One tool bar will have items for "Guidebooks (w/9 item popup menu), Audios (w/9 item popup menu), Videos (w/9 item popup menu), Journal (w/2 item popup menu), and Goals."
A second tool bar will have items for "Blog, Community, Events, Sovereignty, Foundation, and Influence."
The tool bars should have icons and text.
There should be two status panel, one for Audio and one for Video.
The status panels should show the name of the audio or video that is opened, have check boxes for: Add to favorites, Come back, and Done, and have links for: Audios, Top Posts, Post, and Tips.

```html
<!DOCTYPE html>
<html lang="en">
<head>
<meta charset="utf-8">
<title>Quiet Harvest Control Panel</title>
<link rel="stylesheet" href="https://fonts.googleapis.com/css2?family=Marcellus+SC&display=swap">
<style>
:root{
  --bg-top:#f7f8e6;
  --bg-bottom:#dcddc0;
  --frame:#6e6e6e;
  --frame-dark:#4f4f4f;
  --frame-light:#9a9a9a;
  --bar-light:#f4f4f4;
  --bar-mid:#d9d9d9;
  --header-light:#c9c9c9;
  --header-dark:#8f8f8f;
  --body:#e3e3e3;
  --ink:#111;
  --link:#1b1b1b;
  --check:#2b3f8c;
  --check-bg:#f8f8fb;
  --check-edge:#6b6b7a;
}
*{box-sizing:border-box;margin:0;padding:0}
html,body{width:1200px;height:900px;overflow:hidden}
body{
  background:linear-gradient(180deg,var(--bg-top),var(--bg-bottom));
  font-family:"Marcellus SC",serif;
  color:var(--ink);
  position:relative;
}
.panel{
  position:absolute;left:386px;top:146px;width:426px;height:598px;
  background:var(--frame);
  border:1px solid var(--frame-dark);
  box-shadow:0 2px 8px rgba(0,0,0,.18);
}
.panel-top{
  position:absolute;left:0;top:0;width:100%;height:36px;
  background:linear-gradient(180deg,#7b7b7b,#666);
}
.panel-top svg{position:absolute;left:0;top:0}
.close-btn{
  position:absolute;right:6px;top:4px;width:24px;height:24px;border-radius:50%;
  background:radial-gradient(circle at 40% 35%,#fff,#d8d8d8);
  border:1px solid #999;
}
.toolbar{
  position:absolute;left:2px;right:2px;display:flex;justify-content:space-around;align-items:center;
  background:linear-gradient(180deg,var(--bar-light),var(--bar-mid));
}
.toolbar-main{top:36px;height:66px}
.toolbar-foot{bottom:6px;height:70px}
.tool-icon{width:44px;height:44px;border-radius:6px}
.strip{position:absolute;left:0;width:100%}
.section-head{
  position:absolute;left:4px;right:4px;height:30px;display:flex;align-items:center;gap:8px;
  padding-left:8px;font-size:17px;letter-spacing:.5px;
  background:linear-gradient(180deg,var(--header-light),var(--header-dark));
  border-top:1px solid #e8e8e8;
}
.section-head .tri{width:0;height:0}
.tri-right{border-top:6px solid transparent;border-bottom:6px solid transparent;border-left:8px solid #222}
.tri-down{border-left:6px solid transparent;border-right:6px solid transparent;border-top:8px solid #222}
.section-head .track{margin-left:48px}
.status{
  position:absolute;left:4px;right:4px;height:150px;
  background:linear-gradient(180deg,#f1f1f1,var(--body));
  padding:10px 14px 0 14px;
}
.status-row{display:flex;justify-content:space-between;align-items:center;height:31px;font-size:19px;font-weight:bold;text-shadow:0 0 .4px #000}
.check{
  width:22px;height:22px;border:1px solid var(--check-edge);background:var(--check-bg);
  display:flex;align-items:center;justify-content:center
}
.links{display:flex;justify-content:space-between;margin-top:10px;font-size:22px;color:var(--link)}
</style>
</head>
<body>
<main class="panel" aria-label="Quiet Harvest control panel">
  <div class="panel-top">
    <svg width="120" height="36" aria-hidden="true"><polygon points="0,0 70,0 120,36 0,36" fill="#9a9a9a"/></svg>
    <div class="close-btn" aria-label="Close">
      <svg width="22" height="22" viewBox="0 0 22 22"><path d="M7 7l8 8M15 7l-8 8" stroke="#555" stroke-width="2.4" stroke-linecap="round"/></svg>
    </div>
  </div>

  <nav class="toolbar toolbar-main" aria-label="Modules">
    <div class="tool-icon" role="img" aria-label="Welcome icon" style="background:radial-gradient(circle,#f7b23a,#e0742a)"></div>
    <div class="tool-icon" role="img" aria-label="Guidebooks icon" style="background:linear-gradient(#fafafa,#8a8a8a)"></div>
    <div class="tool-icon" role="img" aria-label="Audios icon" style="background:linear-gradient(#d8d8d8,#8c8c8c)"></div>
    <div class="tool-icon" role="img" aria-label="Videos icon" style="background:linear-gradient(#b0b0b0,#3d3d3d)"></div>
    <div class="tool-icon" role="img" aria-label="Journal icon" style="background:linear-gradient(#e4e4e4,#7c6e56)"></div>
    <div class="tool-icon" role="img" aria-label="Goals icon" style="background:linear-gradient(#8ccf7a,#2d5a2b)"></div>
    <div class="tool-icon" role="img" aria-label="Profile icon" style="background:linear-gradient(#6aa6e4,#e8c448)"></div>
  </nav>

  <svg class="strip" style="top:102px" width="426" height="18" aria-hidden="true">
    <rect width="426" height="18" fill="#6a6a6a"/>
    <polygon points="0,0 60,0 80,18 0,18" fill="#5a5a5a"/>
  </svg>

  <div class="section-head" style="top:114px"><span class="tri tri-right"></span>Guide Book:</div>

  <div class="section-head" style="top:150px"><span class="tri tri-down"></span>Audio:<span class="track">Departure 1:</span></div>
  <section class="status" style="top:180px" aria-label="Audio status">
    <div class="status-row">Come back<span class="check"><svg width="16" height="16" viewBox="0 0 16 16"><path d="M3 8l3 4 7-9" stroke="var(--check)" stroke-width="2.4" fill="none"/></svg></span></div>
    <div class="status-row">Done<span class="check"><svg width="16" height="16" viewBox="0 0 16 16"><path d="M3 8l3 4 7-9" stroke="var(--check)" stroke-width="2.4" fill="none"/></svg></span></div>
    <div class="status-row">Add to favorites<span class="check"><svg width="16" height="16" viewBox="0 0 16 16"><path d="M3 8l3 4 7-9" stroke="var(--check)" stroke-width="2.4" fill="none"/></svg></span></div>
    <div class="links"><span>Audios</span><span>Top posts</span><span>Post</span><span>Tips</span></div>
  </section>

  <div class="section-head" style="top:326px"><span class="tri tri-down"></span>Video:<span class="track">Departure 1:</span></div>
  <section class="status" style="top:356px" aria-label="Video status">
    <div class="status-row">Come back<span class="check"><svg width="16" height="16" viewBox="0 0 16 16"><path d="M3 8l3 4 7-9" stroke="var(--check)" stroke-width="2.4" fill="none"/></svg></span></div>
    <div class="status-row">Done<span class="check"><svg width="16" height="16" viewBox="0 0 16 16"><path d="M3 8l3 4 7-9" stroke="var(--check)" stroke-width="2.4" fill="none"/></svg></span></div>
    <div class="status-row">Add to favorites<span class="check"><svg width="16" height="16" viewBox="0 0 16 16"><path d="M3 8l3 4 7-9" stroke="var(--check)" stroke-width="2.4" fill="none"/></svg></span></div>
    <div class="links"><span>Audios</span><span>Top posts</span><span>Post</span><span>Tips</span></div>
  </section>

  <nav class="toolbar toolbar-foot" aria-label="Community">
    <div class="tool-icon" role="img" aria-label="Kudos icon" style="background:linear-gradient(#fff,#cfcfcf);border:1px solid #777"></div>
    <div class="tool-icon" role="img" aria-label="Blog icon" style="background:linear-gradient(#f8a54a,#e0661c)"></div>
    <div class="tool-icon" role="img" aria-label="Community icon" style="background:linear-gradient(#6fb0e6,#e8a23a)"></div>
    <div class="tool-icon" role="img" aria-label="Events icon" style="background:linear-gradient(#f2f2f2,#e06a3a)"></div>
    <div class="tool-icon" role="img" aria-label="Sovereignty icon" style="background:linear-gradient(#dcdcdc,#7a7a7a)"></div>
    <div class="tool-icon" role="img" aria-label="Foundation icon" style="background:linear-gradient(#fff3ec,#e8662c)"></div>
    <div class="tool-icon" role="img" aria-label="Influence icon" style="background:linear-gradient(#9a9a9a,#2e2e2e)"></div>
  </nav>
</main>
</body>
</html>
```